The maple crew

I want it as prefession and attractive as possible we are a lawnmowing business

Phone number 605-318-2264
Name- Carlos Whitfield
Email- themaplecrewsd@fernpost.com

```html
<!DOCTYPE html>
<html lang="en">
<head>
<meta charset="utf-8">
<title>The maple crew – Business Card</title>
<link href="https://fonts.googleapis.com/css2?family=Montserrat:wght@400;500;600;800&display=swap" rel="stylesheet">
<style>
  :root {
    --backdrop: #3a3a3c;
    --paper: #ffffff;
    --forest: #0f4a1e;
    --pine: #0c5a35;
    --leaf: #5cba45;
    --ink: #1d1d1d;
  }
  * { box-sizing: border-box; margin: 0; padding: 0; }
  html, body {
    width: 1200px; height: 1200px; overflow: hidden;
    background: var(--backdrop);
    font-family: "Montserrat", Arial, sans-serif;
  }
  .sheet {
    position: relative; width: 1200px; height: 1200px;
  }
  .card {
    position: absolute; left: 220px;
    width: 760px; height: 434px;
    border-radius: 34px; overflow: hidden;
    box-shadow: 0 14px 30px rgba(0,0,0,0.45);
  }
  .card--front { top: 120px; background: var(--paper); }
  .card--back { top: 646px; background: var(--forest); border-bottom: 4px solid var(--leaf); }

  .brand {
    font-weight: 800; text-transform: uppercase; letter-spacing: 1px; line-height: 1;
  }
  .card--front .brand {
    position: absolute; top: 78px; right: 60px;
    font-size: 38px; color: var(--pine);
  }
  .card--back .brand {
    position: absolute; top: 50%; left: 50%; transform: translate(-50%, -50%);
    font-size: 58px; color: var(--paper); white-space: nowrap;
  }

  .contact { position: absolute; left: 60px; top: 222px; color: var(--ink); }
  .contact__name {
    font-size: 34px; font-weight: 600; color: var(--leaf);
    text-transform: uppercase; letter-spacing: 1px; line-height: 1.05;
  }
  .contact__role {
    font-size: 19px; font-weight: 400; text-transform: uppercase;
    letter-spacing: 1px; margin-bottom: 14px;
  }
  .contact__line {
    display: flex; align-items: center; gap: 12px;
    font-size: 21px; font-weight: 400; margin-top: 6px;
  }
  .contact__line svg { width: 24px; height: 24px; flex: none; }

  .card__band { position: absolute; left: 0; bottom: 0; width: 760px; height: 44px; }
</style>
</head>
<body>
<main class="sheet">
  <section class="card card--front" aria-label="Card front">
    <div class="brand">The maple crew</div>
    <div class="contact">
      <div class="contact__name">Carlos Whitfield</div>
      <div class="contact__role">Owner</div>
      <div class="contact__line">
        <svg viewBox="0 0 24 24" aria-hidden="true"><path fill="#5cba45" d="M6.6 10.8a15.1 15.1 0 0 0 6.6 6.6l2.2-2.2a1 1 0 0 1 1-.25 11.4 11.4 0 0 0 3.6.57 1 1 0 0 1 1 1V20a1 1 0 0 1-1 1A17 17 0 0 1 3 4a1 1 0 0 1 1-1h3.5a1 1 0 0 1 1 1c0 1.25.2 2.45.57 3.57a1 1 0 0 1-.25 1z"/></svg>
        <span>605-318-2264</span>
      </div>
      <div class="contact__line">
        <svg viewBox="0 0 24 24" aria-hidden="true"><path fill="#5cba45" d="M2 5h20v14H2z"/><path fill="none" stroke="#fff" stroke-width="1.6" d="M2 5l10 8 10-8M2 19l7-7M22 19l-7-7"/></svg>
        <span>themaplecrewsd@fernpost.com</span>
      </div>
    </div>
    <svg class="card__band" viewBox="0 0 760 44" preserveAspectRatio="none" aria-hidden="true">
      <polygon points="0,26 470,26 462,44 0,44" fill="var(--leaf)"/>
      <polygon points="478,8 760,8 760,44 470,44" fill="var(--pine)"/>
    </svg>
  </section>

  <section class="card card--back" aria-label="Card back">
    <div class="brand">The maple crew</div>
  </section>
</main>
</body>
</html>
```